Kestrel Plumbing business card full re design & logo design

Kestrel Plumbing is a Sydney based mechanical plumbing contractor company.
We would like a full redesign with new logo etc which we can take to a future website, uniforms, vehicle sign writing etc.
Blue is my preferred choice of colour but i would be open to see a couple of alternatives thrown in the mix to see how they compare. I am open to see on white cards, black cards etc. Open to many new ideas.
Please see attached original business cards which have been used for the last 5 years.

Target Market(s)

Mechanical services industry.

Industry/Entity Type

Plumbing

Contact Information for Business Card

Dale Fenmore
Director

Mob: 0427 596 418
Email: dale@kestrelplumbing-demo.net.au
PO BOX 782
Merrow Park NSW 2170
Lic: 518604k

Logo Text

Kestrel Plumbing

Font styles to use
Sans Serif

Colors
0655a3
3276b5
0792cd
33a6d7
85cae6
000000
333333
474747

Requirements
Must have
• Things that make it very professional and very well presented.
Nice to have
• Same description or very similar to attached uploaded file
Should not have
• Anything that makes it look unprofessional or cartoony.

```html
<!DOCTYPE html>
<html lang="en">
<head>
<meta charset="utf-8">
<title>Kestrel Plumbing – Business Card</title>
<link href="https://fonts.googleapis.com/css2?family=Arimo:wght@400&display=swap" rel="stylesheet">
<style>
  :root {
    --page-bg: #ffffff;
    --card-blue: #0792cd;
    --ink-light: #ffffff;
    --rule: #85cae6;
  }
  * { margin: 0; padding: 0; box-sizing: border-box; }
  html, body {
    width: 1200px;
    height: 1000px;
    overflow: hidden;
    background: var(--page-bg);
    font-family: "Arimo", Arial, sans-serif;
    color: var(--ink-light);
  }
  .canvas { position: relative; width: 1200px; height: 1000px; }
  .card {
    position: absolute;
    left: 292px;
    width: 615px;
    height: 369px;
    background: var(--card-blue);
    overflow: hidden;
  }
  .card--front { top: 109px; }
  .card--back { top: 500px; }

  .brand {
    position: absolute;
    display: flex;
    align-items: center;
    font-weight: 400;
    color: var(--ink-light);
    white-space: nowrap;
  }
  .brand__dot {
    border-radius: 50%;
    background: var(--ink-light);
    flex: none;
  }
  .card--front .brand { left: 0; right: 0; top: 118px; justify-content: center; gap: 18px; font-size: 38px; }
  .card--front .brand__dot { width: 46px; height: 46px; }
  .card--back .brand { left: 62px; top: 276px; gap: 14px; font-size: 26px; }
  .card--back .brand__dot { width: 32px; height: 32px; }

  .front-rule {
    position: absolute;
    left: 81px; top: 258px;
    width: 455px; height: 1px;
    background: var(--rule);
  }
  .website {
    position: absolute;
    left: 0; right: 0; top: 283px;
    text-align: center;
    font-size: 14px;
  }

  .person { position: absolute; left: 62px; top: 52px; }
  .person__name { font-size: 29px; line-height: 32px; }
  .person__role { font-size: 18px; line-height: 20px; letter-spacing: 0.5px; padding-left: 2px; }
  .back-rule {
    position: absolute;
    left: 62px; top: 121px;
    width: 289px; height: 1px;
    background: var(--rule);
  }
  .contact {
    position: absolute;
    left: 62px; top: 132px;
    list-style: none;
    font-size: 15px;
  }
  .contact li { position: relative; height: 27px; line-height: 20px; white-space: nowrap; }
  .contact__label { display: inline-block; }
  .contact__label--wide { width: 71px; }
  .contact__licence { position: absolute; left: 191px; top: 0; }
</style>
</head>
<body>
<main class="canvas">
  <section class="card card--front" aria-label="Business card front">
    <div class="brand"><span class="brand__dot"></span>Kestrel Plumbing</div>
    <div class="front-rule"></div>
    <p class="website">www.kestrelplumbing-demo.net.au</p>
  </section>

  <section class="card card--back" aria-label="Business card back">
    <div class="person">
      <p class="person__name">Dale Fenmore</p>
      <p class="person__role">Director</p>
    </div>
    <div class="back-rule"></div>
    <ul class="contact">
      <li>Email: dale@kestrelplumbing-demo.net.au</li>
      <li><span class="contact__label contact__label--wide">Mobile:</span>0427 596 418</li>
      <li>PO BOX 782</li>
      <li>Merrow Park NSW 2170<span class="contact__licence">Lic: 518604k</span></li>
    </ul>
    <div class="brand"><span class="brand__dot"></span>Kestrel Plumbing</div>
  </section>
</main>
</body>
</html>
```